Menu Revamp- Simplify and highlight

Redesign the current menu while maintaining the existing dimensions to fit within a window display. The goal is to improve readability, declutter the layout, and make price visibility more subtle while ensuring the design remains easy to update annually.

Current Challenges:
• The menu feels cluttered, making it difficult for customers to quickly find what they want.
• Prices stand out too much, drawing more attention than necessary.
• Editing and updating the menu each year is cumbersome and needs simplification.

Requirements:
• Maintain the current specifications and dimensions to ensure it fits in the designated window space.
• Improve readability by organizing the menu in a cleaner, more structured format.
• Adjust the price formatting so it is visible but not the primary focus.
• Ensure the new design allows for easy annual updates, minimizing the need for complete redesigns each year.
• Consider a font and layout that enhance clarity while maintaining the brand’s aesthetic.

Additional Considerations:
• Potential use of color or sectioning to group similar items for better flow.
• A design that aligns with the overall brand identity and customer expectations.
• Digital-friendly formatting for quick edits without affecting the overall structure.

This redesign should make the menu more visually appealing, user-friendly, and practical for future updates while keeping within the original space constraints.
Updates

Gathering more feedback

Target Market(s)

Families and people coming to vacation

Industry/Entity Type

food

Font styles to use
Serif
Sans Serif

Colors
0054AA
0677BA
7BADD7
CADEEF
E8F1F8
F0912C
F2A743
F7CA91
FBE8D2
FDF5EE
EE7325
F08F49
F5BC92
FAE3D3
FDF4ED
EB3D1F
EC4F4E
F09395
F8D3D4
FCEDEE

Requirements
Must have
• all the details, names, and such need to stay. I need it organized better and easier to view and read
Nice to have
• it would be nice if the layers were easier to modify and change year to year.
Should not have
• do not remove details. Please make pricing less prevelant.

```html
<!DOCTYPE html>
<html lang="en">
<head>
<meta charset="utf-8">
<title>Sandy Toes – Food Menu</title>
<link href="https://fonts.googleapis.com/css2?family=Poppins:wght@400;500;600;700&display=swap" rel="stylesheet">
<style>
  :root{
    --blue-deep:#0054AA;
    --blue:#0677BA;
    --sky-top:#7fd3ee;
    --sky-mid:#d3eef7;
    --sand:#f7ca91;
    --sand-deep:#f5b772;
    --orange:#F0912C;
    --orange-price:#F08F49;
    --red:#EB3D1F;
    --red-title:#EC4F4E;
    --green:#3f8c12;
    --green-title:#2e8a0f;
    --ink:#2c2c2c;
    --muted:#687a8c;
    --stage:#4d4d4d;
  }
  *{margin:0;padding:0;box-sizing:border-box}
  html,body{width:1200px;height:946px;overflow:hidden;background:var(--stage)}
  body{font-family:"Poppins",sans-serif;color:var(--ink)}
  .stage{position:relative;width:1200px;height:946px;overflow:hidden}
  .menu{
    position:absolute;left:0;top:22px;width:1284px;height:964px;
    transform:scale(0.93458);transform-origin:0 0;
    background:linear-gradient(180deg,var(--sky-top) 0%,#a9e0f3 25%,var(--sky-mid) 42%,#e6eef0 52%,#fbe3bd 66%,var(--sand) 85%,var(--sand-deep) 100%);
    overflow:hidden;
  }
  .art{position:absolute;border-radius:10px}
  .leaves{background:radial-gradient(ellipse at 50% 10%,#3f9a34 0%,#5fb846 45%,rgba(95,184,70,0) 72%)}
  .sign{background:linear-gradient(180deg,#8a5533,#6b3d22);border-radius:14px;box-shadow:0 0 0 14px rgba(74,170,60,.35)}
  .starfish{background:radial-gradient(circle,#e23a28 0%,#e8513a 50%,rgba(232,81,58,0) 72%)}
  .food-left{background:radial-gradient(ellipse at 50% 55%,#c9833c 0%,#e2a35a 45%,rgba(226,163,90,0) 75%)}
  .food-mid{background:radial-gradient(ellipse at 45% 55%,#d36b3a 0%,#8fb35a 50%,rgba(143,179,90,0) 76%)}
  .drinks{background:radial-gradient(ellipse at 50% 55%,#f4a02a 0%,#f8c94a 45%,rgba(248,201,74,0) 75%)}

  .brand{position:absolute;left:532px;top:48px;width:225px;text-align:center;
    font-weight:700;font-size:40px;line-height:44px;color:var(--red)}

  .bar{position:absolute;height:25px;padding:0 8px;color:#fff;font-weight:500;font-size:15.5px;line-height:25px;letter-spacing:.2px;white-space:nowrap}
  .bar.red{background:var(--red)}
  .bar.blue{background:var(--blue-deep)}
  .bar.orange{background:var(--orange)}
  .bar.green{background:var(--green)}

  .name{position:absolute;font-weight:600;font-size:12.5px;line-height:14px;text-transform:uppercase;white-space:nowrap}
  .name.red{color:var(--red-title)}
  .name.orange{color:var(--orange)}
  .name.blue{color:var(--blue-deep)}
  .name.green{color:var(--green-title)}
  .desc{position:absolute;font-size:8.6px;line-height:10.6px;color:var(--ink)}
  .note{position:absolute;font-size:8.6px;line-height:10.6px;color:var(--ink);white-space:nowrap}
  .note.dot::before{content:"";display:inline-block;width:4px;height:4px;border-radius:50%;background:var(--orange-price);margin:0 6px 1px 0}
  .note.dot.blue::before{background:var(--blue)}
  .note.dot.green::before{background:var(--green)}

  .price{position:absolute;font-weight:600;font-size:12.5px;line-height:14px;text-align:right;white-space:nowrap}
  .price sup{font-size:7px;vertical-align:5px;margin-right:1px}
  .price.orange{color:var(--orange-price)}
  .price.red{color:var(--red)}
  .price.blue{color:var(--blue-deep)}
  .price.green{color:var(--green-title)}
  .price.big{font-size:14px}

  .pills{position:absolute;display:flex;gap:10px}
  .pill{display:flex;height:15px;border-radius:8px;overflow:hidden;background:#fff;font-size:8.5px;line-height:15px;font-weight:600}
  .pill .size{padding:0 5px;color:var(--ink)}
  .pill .cost{padding:0 6px 0 5px;background:var(--orange-price);color:#fff;border-radius:0 8px 8px 0}
  .pill .cost.red{background:var(--red)}
  .pill sup{font-size:6px;vertical-align:3px}

  .rule{position:absolute;border-top:1px dotted #8c9aa6;height:0}

  .shakes-head{position:absolute;left:920px;top:292px;font-weight:600;font-size:21px;color:var(--blue-deep);letter-spacing:.3px}

  .sides{position:absolute;left:480px;top:822px;display:flex;gap:14px}
  .side{font-weight:500;font-size:11.5px;line-height:11.5px;color:var(--muted);text-transform:uppercase}
  .side .cost{display:block;margin-top:9px;font-weight:600;font-size:12.5px;color:var(--red)}
  .side sup{font-size:7px;vertical-align:4px}

  .sizes{position:absolute;left:918px;top:728px;font-weight:600;font-size:13px;white-space:nowrap;color:var(--ink)}
  .sizes span{margin-right:10px}
  .sizes sup{font-size:7px;color:var(--orange-price);vertical-align:5px}
  .sizes b{color:var(--orange-price);font-weight:600}

  .flavors{position:absolute;list-style:none;font-size:7.8px;line-height:10.1px;color:#3a3a3a;white-space:nowrap}
  .flavors li::before{content:"Y";color:#9aa;font-size:7px;margin-right:4px}
</style>
</head>
<body>
<div class="stage">
<main class="menu">

  <div class="art leaves" style="left:372px;top:-20px;width:220px;height:120px" role="img" aria-label="Palm fronds hanging from the top edge"></div>
  <div class="art leaves" style="left:772px;top:-20px;width:150px;height:100px" role="img" aria-label="Palm fronds hanging from the top edge"></div>
  <div class="brand">Sandy Toes</div>
  <div class="art sign" style="left:500px;top:175px;width:285px;height:130px" role="img" aria-label="Wooden sign reading Food Menu framed by tropical leaves, flowers and starfish"></div>
  <div class="art starfish" style="left:352px;top:782px;width:90px;height:110px" role="img" aria-label="Red starfish on the sand"></div>
  <div class="art food-left" style="left:22px;top:872px;width:260px;height:100px" role="img" aria-label="Photo of fries, onion rings and a cheeseburger"></div>
  <div class="art food-mid" style="left:542px;top:867px;width:295px;height:105px" role="img" aria-label="Photo of grilled shrimp and a pulled pork salad plate"></div>
  <div class="art drinks" style="left:1142px;top:832px;width:115px;height:115px" role="img" aria-label="Photo of two iced citrus drinks"></div>

  <!-- LEFT COLUMN -->
  <section class="burgers">
    <div class="bar red" style="left:47px;top:55px">1/4 HAND SMASHED BURGERS</div>
    <p class="desc" style="left:50px;top:83px;width:270px">All of our burgers are 100% hand-smashed ground chuck beef and served on a toasted Artisan bun.</p>

    <h3 class="name red" style="left:50px;top:110px">The Rock Cheeseburger</h3>
    <div class="pills" style="left:50px;top:128px">
      <span class="pill"><span class="size">Single</span><span class="cost"><sup>$</sup>7.49</span></span>
      <span class="pill"><span class="size">Double</span><span class="cost"><sup>$</sup>1.99</span></span>
      <span class="pill"><span class="size">Triple</span><span class="cost red">+<sup>$</sup>3.98</span></span>
      <span class="pill"><span class="size">Quad</span><span class="cost red">+<sup>$</sup>5.97</span></span>
    </div>
    <p class="note" style="left:60px;top:147px">Add Bacon or Shredded Brisket</p>
    <p class="price red" style="right:902px;top:148px"><sup>$</sup>1.49/<sup>$</sup>2.49</p>

    <h3 class="name red" style="left:50px;top:171px">Spinnacker Barbecue</h3>
    <div class="pills" style="left:231px;top:170px">
      <span class="pill"><span class="size">Single</span><span class="cost"><sup>$</sup>7.49</span></span>
      <span class="pill"><span class="size">Double</span><span class="cost"><sup>$</sup>1.99</span></span>
    </div>
    <p class="note" style="left:50px;top:189px">Bacon, Onion Ring, Cheddar Cheese and Marlo's Sassy BBQ Sauce.</p>
    <p class="note dot" style="left:50px;top:206px">Make it Spicy with Jalapenos and Queso</p>
    <p class="price red" style="right:902px;top:203px"><sup>$</sup>.99</p>
    <p class="note dot" style="left:50px;top:222px">Add Shredded Brisket</p>
    <p class="price red" style="right:902px;top:221px"><sup>$</sup>2.49</p>
    <div class="rule" style="left:50px;top:236px;width:332px"></div>

    <h3 class="name red" style="left:50px;top:252px">South Eden Hamburger</h3>
    <div class="pills" style="left:231px;top:255px">
      <span class="pill"><span class="size">Single</span><span class="cost"><sup>$</sup>6.99</span></span>
      <span class="pill"><span class="size">Double</span><span class="cost"><sup>$</sup>1.99</span></span>
    </div>
    <p class="note dot" style="left:50px;top:267px">Add Bacon or Shredded Brisket</p>

    <h3 class="name red" style="left:50px;top:295px">Gil's Avocado Queso</h3>
    <div class="pills" style="left:231px;top:295px">
      <span class="pill"><span class="size">Single</span><span class="cost"><sup>$</sup>8.99</span></span>
      <span class="pill"><span class="size">Double</span><span class="cost"><sup>$</sup>1.99</span></span>
    </div>
    <p class="note dot" style="left:50px;top:322px">Avocado,Tomato, and White Queso Cheese</p>
    <p class="price red" style="right:902px;top:319px"><sup>$</sup>1.49/<sup>$</sup>2.49</p>

    <h3 class="name red" style="left:50px;top:354px;line-height:13px">The Garden City<br>Hot Honey</h3>
    <div class="pills" style="left:231px;top:358px">
      <span class="pill"><span class="size">Single</span><span class="cost"><sup>$</sup>8.99</span></span>
      <span class="pill"><span class="size">Double</span><span class="cost"><sup>$</sup>1.99</span></span>
    </div>
    <p class="note" style="left:50px;top:383px">Jalapenos, Hot Honey, Pepperjack Cheese, Bacon, Lettuce, Tomato</p>

    <h3 class="name red" style="left:50px;top:410px">Cisco Beach Garlic Parm</h3>
    <div class="pills" style="left:231px;top:409px">
      <span class="pill"><span class="size">Single</span><span class="cost"><sup>$</sup>8.99</span></span>
      <span class="pill"><span class="size">Double</span><span class="cost"><sup>$</sup>1.99</span></span>
    </div>
    <p class="note" style="left:50px;top:427px">Creamy Garlic Parmesean Sauce, Onion, Lettuce</p>

    <h3 class="name red" style="left:50px;top:448px">Hot Springs Double Grilled Cheese</h3>
    <div class="pills" style="left:305px;top:448px">
      <span class="pill"><span class="size">Double</span><span class="cost"><sup>$</sup>10.69</span></span>
    </div>
    <p class="desc" style="left:50px;top:466px;width:320px">Two Cheesy Patties, a Grilled Cheese Sandwich, and Classic Burger Toppings in One Burger</p>
  </section>

  <section class="wraps">
    <div class="bar blue" style="left:47px;top:509px">RAINBOW COVE WRAPS</div>
    <p class="price blue" style="right:904px;top:514px"><sup>$</sup>8.99</p>
    <p class="desc" style="left:50px;top:537px;width:320px">All wraps are made to order with fresh grilled chicken or shrimp and rolled in a Tomato Tortilla</p>

    <h3 class="name blue" style="left:50px;top:563px">Avocado Chicken Ranch</h3>
    <p class="desc" style="left:50px;top:577px;width:310px">Smoked Chicken, Bacon, Avocado, Lettuce, Spinach and  Tomato with Ranch Dressing</p>

    <h3 class="name blue" style="left:50px;top:606px">BBQ Chicken Bacon</h3>
    <p class="desc" style="left:50px;top:620px;width:320px">Smoked Chicken, Bacon, Cheddar Cheese, Red Onion, Lettuce and Tomato with Marlo's Raspberry BBQ Sauce</p>

    <h3 class="name blue" style="left:50px;top:650px">Chipotle Shrimp</h3>
    <p class="note" style="left:50px;top:664px">Fried Shrimp, Tomato and Lettuce with Chili Lime Aioli</p>
    <p class="note dot blue" style="left:52px;top:684px">Add Avocado or Bacon</p>
    <p class="price blue big" style="right:902px;top:679px">$.99 / $1.49</p>
  </section>

  <section class="kids">
    <div class="bar red" style="left:47px;top:718px">SEASHELL FINDERS (KIDS)</div>
    <p class="price red" style="right:902px;top:720px"><sup>$</sup>7.99</p>
    <p class="note" style="left:50px;top:746px">Includes Side of Fries or Onion Rings and 12 oz Drink</p>
    <h3 class="name red" style="left:50px;top:762px">Little Burger</h3>
    <p class="note" style="left:50px;top:775px">Slider size burger with pickles &amp; ketchup. Add cheese for free.</p>
    <h3 class="name red" style="left:50px;top:791px">Pulled Pork Sandwich</h3>
    <p class="note" style="left:50px;top:804px">1/2 of a regular sandwich with sweet raspberry BBQ sauce.</p>
    <h3 class="name red" style="left:50px;top:826px">Corn Dog</h3>
    <h3 class="name red" style="left:50px;top:842px">Grilled Cheese</h3>
  </section>

  <!-- MIDDLE COLUMN -->
  <section class="pulled-pork">
    <div class="bar orange" style="left:478px;top:325px;width:233px">PULLED PORK &amp; SHRIMP</div>
    <p class="desc" style="left:481px;top:357px;width:240px">Our Pulled Pork is house smoked and slow roasted. All pork and shrimp are served on a Ciabatta Bun.</p>

    <h3 class="name orange" style="left:481px;top:386px">Siddoway Pump Pulled Pork</h3>
    <p class="note" style="left:481px;top:400px">Pulled Pork and Marlo's Sweet Raspberry BBQ Sauce</p>
    <p class="price orange" style="right:480px;top:397px"><sup>$</sup>8.49</p>
    <div class="rule" style="left:481px;top:413px;width:322px"></div>

    <h3 class="name orange" style="left:481px;top:418px">2nd Point Sweet Pulled Pork</h3>
    <p class="note" style="left:481px;top:432px">Pulled Pork, Marlo's Sweet Raspberry BBQ Sauce and Coleslaw</p>
    <p class="price orange" style="right:480px;top:428px"><sup>$</sup>8.49</p>
    <div class="rule" style="left:481px;top:445px;width:322px"></div>

    <h3 class="name orange" style="left:481px;top:450px">1st Point Spicy Pulled Pork</h3>
    <p class="desc" style="left:481px;top:464px;width:250px">Pulled Pork, Marlo's Sassy BBQ Sauce, Chopped Bacon, Pepperjack Cheese and Jalapenos</p>
    <p class="price orange" style="right:480px;top:461px"><sup>$</sup>8.49</p>
    <div class="rule" style="left:481px;top:489px;width:322px"></div>

    <h3 class="name orange" style="left:481px;top:496px">Fish Haven Shrimp Po' Boy</h3>
    <p class="desc" style="left:481px;top:510px;width:180px">Fried Shrimp, Tomato and Lettuce with Chili Lime Aioli</p>
    <p class="price orange" style="right:480px;top:507px">$.99 / $1.49 EA</p>
    <p class="note" style="left:481px;top:534px">Add Avocado or Bacon -</p>
  </section>

  <section class="brisket">
    <div class="bar red" style="left:478px;top:550px;width:234px">SHREDDED BRISKET</div>
    <p class="desc" style="left:481px;top:578px;width:270px">Our Shredded Brisket is smoked, braised, and shredded. Served on Ciabatta Buns.</p>

    <h3 class="name red" style="left:481px;top:603px">Siddoway Pump Brisket</h3>
    <p class="note" style="left:481px;top:617px">Brisket and Marlo's Sweet Raspberry BBQ Sauce</p>
    <p class="price red" style="right:480px;top:613px"><sup>$</sup>9.99</p>
    <div class="rule" style="left:481px;top:630px;width:322px"></div>

    <h3 class="name red" style="left:481px;top:637px">2nd Point Sweet Brisket</h3>
    <p class="note" style="left:481px;top:651px">Brisket, Marlo's Sweet Raspberry BBQ Sauce and Coleslaw</p>
    <p class="price red" style="right:480px;top:647px"><sup>$</sup>10.99</p>
    <div class="rule" style="left:481px;top:664px;width:322px"></div>

    <h3 class="name red" style="left:481px;top:671px">1st Point Spicy Brisket</h3>
    <p class="desc" style="left:481px;top:685px;width:250px">Brisket, Marlo's Sassy BBQ Sauce, Chopped Bacon, Pepperjack Cheese and Jalapenos</p>
    <p class="price red" style="right:480px;top:682px"><sup>$</sup>10.99</p>
    <div class="rule" style="left:481px;top:709px;width:322px"></div>
  </section>

  <section class="fries">
    <div class="bar blue" style="left:478px;top:723px;width:282px">RENDEZVOUS BEACH LOADED FRIES</div>
    <p class="desc" style="left:481px;top:752px;width:240px">Brisket, Marlo's Sassy BBQ Sauce, Chopped Bacon, Pepperjack Cheese and Jalapenos</p>
    <p class="note dot blue" style="left:481px;top:774px">Substitute Pork for Shredded Brisket</p>
    <p class="price blue" style="right:478px;top:768px"><sup>$</sup>2.99</p>
  </section>

  <section class="sides-section">
    <div class="bar red" style="left:478px;top:792px;width:56px">SIDES</div>
    <div class="sides">
      <div class="side">Sandy's<br>Fries<span class="cost"><sup>$</sup>4.99</span></div>
      <div class="side">Onion<br>Rings<span class="cost"><sup>$</sup>5.69</span></div>
      <div class="side">Creamy<br>Coleslaw<span class="cost"><sup>$</sup>3.99</span></div>
      <div class="side">Side<br>Salad<span class="cost"><sup>$</sup>3.99</span></div>
      <div class="side">Mac N<br>Cheese Bites<span class="cost"><sup>$</sup>5.29</span></div>
    </div>
  </section>

  <!-- RIGHT COLUMN -->
  <section class="salads">
    <div class="bar green" style="left:916px;top:57px;width:234px">GREEN SHORE SALADS</div>
    <p class="price green" style="right:42px;top:64px"><sup>$</sup>9.99</p>

    <h3 class="name green" style="left:918px;top:87px">East Side Apple</h3>
    <p class="desc" style="left:918px;top:101px;width:320px">Chopped Apples, Candied Walnuts, Red Onion and Feta Cheese on Fresh Spinach and Lettuce Medley</p>
    <p class="note" style="left:918px;top:127px">Best with Marlo's Raspberry Vinaigrette.</p>
    <p class="note" style="left:918px;top:140px">Add Chicken Breast</p>
    <p class="price green" style="right:42px;top:136px"><sup>$</sup>8.49</p>

    <h3 class="name green" style="left:918px;top:160px">Big Creek Chicken Avocado</h3>
    <p class="desc" style="left:918px;top:174px;width:320px">Smoked Chicken, Crumbled Bacon, Avocado, Red Onion and Diced Tomatoes on Lettuce Medley.</p>
    <p class="note" style="left:918px;top:200px">Best with Ranch Dressing</p>
    <div class="rule" style="left:918px;top:217px;width:322px"></div>

    <h3 class="name green" style="left:918px;top:224px">West Side Bacon</h3>
    <p class="desc" style="left:918px;top:238px;width:320px">Pulled Pork, Crumbled Bacon, Candied Walnuts, Feta Cheese and Red Onion on Spinach and Lettuce Medley</p>
    <p class="note dot green" style="left:920px;top:264px">Best with Ranch Dressing</p>
  </section>

  <section class="shakes">
    <h2 class="shakes-head">SHAKES</h2>
    <div class="bar blue" style="left:916px;top:322px;width:148px">MONSTER STYLE</div>
    <p class="price blue" style="right:42px;top:324px"><sup>$</sup>9.99</p>
    <p class="desc" style="left:918px;top:349px;width:340px">Our Monster Shakes start with our thick and creamy soft serve ice cream. We blend in handcrafted ingredients and top with whipped cream and other treats for a Monster taste! Sold as large only.</p>

    <h3 class="name blue" style="left:918px;top:387px">Marlo's Jammin'Raspberry</h3>
    <p class="desc" style="left:918px;top:401px;width:260px">Made with double raspberries and topped with Marlo's Raspberry Jam and whipped cream.</p>
    <p class="price blue" style="right:42px;top:398px"><sup>$</sup>6.99</p>

    <h3 class="name blue" style="left:918px;top:438px">Apple Pie à la Mode</h3>
    <p class="desc" style="left:918px;top:452px;width:260px">An entire slice of Apple Pie blended with caramel and topped with whipped cream and caramel.</p>
    <p class="price blue" style="right:42px;top:449px"><sup>$</sup>8.99</p>

    <h3 class="name blue" style="left:918px;top:488px">Cookies &amp; Cream Big Scoop</h3>
    <p class="desc" style="left:918px;top:502px;width:260px">A double scoop of chocolate cookies &amp; vanilla wafers and topped with a Big Scoop and whipped cream.</p>
    <p class="price blue" style="right:42px;top:499px"><sup>$</sup>6.99</p>

    <h3 class="name blue" style="left:918px;top:533px">PB Cup PB Chocolate Cake</h3>
    <p class="desc" style="left:918px;top:547px;width:290px">PB cups blended into our rich ice cream. And because we can, we add an entire slice of PB Cup Chocolate Cake on top. With whipped cream.</p>
    <p class="price blue" style="right:42px;top:544px"><sup>$</sup>9.99</p>

    <h3 class="name blue" style="left:918px;top:593px">Raspberry Cheesecake Cheesecake</h3>
    <p class="desc" style="left:918px;top:607px;width:300px">Real raspberries blended with chunks of cheesecake.Topped with an entire piece of Raspberry Cheesecake and whipped cream.</p>
    <p class="price blue" style="right:42px;top:604px"><sup>$</sup>9.99</p>

    <h3 class="name blue" style="left:918px;top:641px">Cookie Cookie Dough</h3>
    <p class="desc" style="left:918px;top:655px;width:280px">A double scoop of cookie dough chunks and topped with a chocolate chip cookie and whipped cream.</p>
    <p class="price blue" style="right:42px;top:652px"><sup>$</sup>9.99</p>
  </section>

  <section class="classic">
    <div class="bar red" style="left:916px;top:699px;width:147px">CLASSIC</div>
    <p class="sizes"><span>WHIPPED CREAM <sup>$</sup><b>.49</b></span><span>SMALL<sup>$</sup><b>4.99</b></span><span>LARGE <sup>$</sup><b>6.49</b></span></p>
    <p class="desc" style="left:918px;top:747px;width:336px">Our Classic Shakes are made with extra creamy soft serve and served in environmental friendly cups. Shake flavors are as listed. No exceptions or combinations.</p>
    <ul class="flavors" style="left:918px;top:788px">
      <li>Famous Raspberry</li><li>Raspberry Cheesecake</li><li>Raspberry Cookies &amp; Cream</li><li>Raspberry Piña Colada</li><li>Raspberry Brownie</li><li>Raspberry Hazelnut Cocoa</li><li>Raspberry Sugar Cookie</li><li>Raspberry Cookie Dough</li><li>Raspberry Marshmallow</li><li>Strawberry</li><li>Strawberry Cheesecake</li><li>Strawberry Cookies &amp; Cream</li><li>Strawberry Brownie</li><li>Strawberry Hazelnut Cocoa</li>
    </ul>
    <ul class="flavors" style="left:1043px;top:788px">
      <li>Strawberry Marshmallow</li><li>Strawberry Cookie</li><li>Strawberry Chocolate</li><li>Piña Colada</li><li>Caramel</li><li>S'mores</li><li>Brownie</li><li>Chocolate Brownie</li><li>Hazelnut Brownie</li><li>Caramel Brownie</li><li>Caramel Cookie</li><li>Chocolate</li><li>Cookies &amp; Cream</li><li>Cookie Dough</li>
    </ul>
    <ul class="flavors" style="left:1162px;top:788px">
      <li>Marshmallow</li><li>Hazelnut Cocoa</li><li>Candy Bar</li><li>Peanut Butter Cup</li><li>Spiced Cookie</li>
    </ul>
  </section>

</main>
</div>
</body>
</html>
```